7s Northgate Harriers Rugby Team

I need a website for a 7s Rugby team. 7s is a form of rugby union and one of the fastest rising sports in the world. Its recent addition to the Olympic games 2016 means that it's meteoric rise will only continue as more countries invest more money in their current programs as they compete for a chance at a medal.

See video for more insight: http://clipvault.example/v/Kx93TqLmWzA

I've started and Elite, Invitation 7s team for U16 boys, U18 boys, and eventually, senior men and junior women's programs to compliment what we already have in place.

We are hoping to attract the top players in across our region of southern Ontario with the goal of created the top 7s rugby program in Canada and providing and ideal pathway for those that want to one day play for Canada.

I want a design that is bright, sharp, professional, flashy and has visual appeal.
Updates

Please see most recent uploaded photos and include these in your designs.  

Additionally, please have a look at the updated colour-scheme.

Thanks

Added Sunday, December 22, 2013

Project Deadline Extended
Reason: Holidays and life have had consumed my energy and time. Would like to take the next week to complete this project with an appropriate amount of time and dedication. Thank you.
Added Sunday, December 29, 2013

Please change images in all designs to include those I have uploaded.

Final decision made by the end of the weekend.

Prize will be increased and split.

Thank you for your patience and continued efforts.

Greatly appreciated.

Added Friday, January 03, 2014

Target Market(s)

Active people between the ages of 14 and 30.

Industry/Entity Type

Union

Font styles to use
Sans Serif

Colors
3176b5
cedeec
f04a50
cee9f6
ceddec
0255a3
5c5c5c
474747

Requirements
Must have
• Highly effective use of visuals; responsive theme or something similar.

Something to encourage players or those interested to want to learn more and potentially register for our affiliated rugby Academy, "Keystone Rugby Canada".

Nice to have
• Connection to YouTube Channel

```html
<!DOCTYPE html>
<html lang="en">
<head>
<meta charset="utf-8">
<title>Northgate Harriers Sevens – Blog</title>
<link rel="stylesheet" href="https://fonts.googleapis.com/css2?family=Open+Sans:wght@400;600;700&display=swap">
<style>
:root{
  --blue:#3176b5;
  --blue-deep:#0255a3;
  --blue-pale:#cee9f6;
  --blue-soft:#cedeec;
  --red:#f04a50;
  --grey:#5c5c5c;
  --grey-dark:#474747;
  --line:#e3e7ec;
  --footer:#1f5a93;
  --footer-text:#d6e4f2;
}
*{box-sizing:border-box;margin:0;padding:0}
html,body{width:1200px;height:2468px;overflow:hidden}
body{font-family:"Open Sans",Arial,sans-serif;color:var(--grey);background:#fff;position:relative;font-size:13px;line-height:1.55}
a{color:inherit;text-decoration:none}
.container{width:1120px;margin:0 auto;position:relative}

/* header */
.site-header{height:108px;background:#fff;border-bottom:1px solid var(--line)}
.site-header .container{height:108px;display:flex;align-items:center;justify-content:space-between}
.brand{display:flex;align-items:center;gap:12px}
.brand-mark{width:22px;height:22px;background:var(--blue-deep)}
.brand-name{font-weight:700;font-size:26px;color:var(--blue-deep);letter-spacing:.5px}
.main-nav{display:flex;height:108px;border-right:1px solid var(--line)}
.main-nav a{width:80px;display:flex;flex-direction:column;align-items:center;justify-content:center;gap:8px;font-size:12px;color:var(--grey);border-left:1px solid var(--line)}
.main-nav a svg{width:20px;height:20px;fill:var(--grey)}
.main-nav a.active{background:var(--blue);color:#fff}
.main-nav a.active svg{fill:#fff}
.main-nav a.search{width:56px}

/* title band */
.page-band{height:76px;background:var(--blue-pale);border-bottom:1px solid var(--blue-soft)}
.page-band .container{height:76px;display:flex;align-items:center}
.page-title{font-size:24px;font-weight:600;color:var(--blue);margin-right:34px}
.page-tagline{font-size:12px;color:#8a9aaa}
.breadcrumb{margin-left:auto;font-size:12px;color:#8a9aaa}
.breadcrumb b{color:var(--blue);font-weight:600}

/* content */
.content{display:flex;justify-content:space-between;padding-top:76px}
.posts{width:800px}
.post{display:flex;height:352px;gap:36px}
.post-media{position:relative;width:432px;height:252px;flex:none}
.photo{position:absolute;inset:0}
.photo.field{background:linear-gradient(180deg,#6e7b63 0%,#9a3a3c 38%,#4f8a3a 62%,#3f7a30 100%)}
.photo.stadium{background:linear-gradient(180deg,#8c95a1 0%,#5d6a76 35%,#4a8a3e 60%,#3d7c32 100%)}
.photo.video{background:linear-gradient(135deg,#d3302f 0%,#b6263a 50%,#7a2b5a 100%)}
.photo.scrum{background:linear-gradient(180deg,#2f6fb2 0%,#cfd8e0 40%,#4f9a3d 70%,#3a7f2e 100%)}
.photo.night{background:linear-gradient(180deg,#1d2428 0%,#2d3a30 45%,#3f8a37 75%,#2f6b29 100%)}
.player-bar{position:absolute;left:0;right:0;bottom:0;height:30px;background:rgba(0,0,0,.8);display:flex;align-items:center;padding:0 10px;gap:10px}
.player-bar .play{width:0;height:0;border-left:12px solid #fff;border-top:7px solid transparent;border-bottom:7px solid transparent}
.player-bar .track{flex:1;height:4px;background:#666}
.player-bar .track i{display:block;width:30%;height:4px;background:#4fb3e8}
.date-badge{position:absolute;left:0;top:0;width:48px;background:var(--blue);color:#fff;text-align:center}
.date-badge .day{display:block;font-size:22px;font-weight:700;line-height:1;padding-top:8px}
.date-badge .month{display:block;font-size:10px;text-transform:uppercase;padding:3px 0 8px}
.date-badge .type{display:flex;align-items:center;justify-content:center;height:42px;background:var(--blue-deep)}
.date-badge .type svg{width:18px;height:18px;fill:#fff}
.post-body{padding-top:34px;flex:1;min-width:0}
.post-title{font-size:18px;font-weight:700;color:var(--blue);text-transform:uppercase;letter-spacing:.3px}
.post-meta{font-size:11px;color:#9aa5b0;margin:2px 0 14px}
.post-meta b{color:var(--blue);font-weight:600}
.post-excerpt{font-size:13px;color:var(--grey);line-height:1.6}
.post-caption{font-size:11px;color:#a5adb5;margin-top:4px}
.read-more{display:block;margin-top:16px;font-size:12px;color:#9aa5b0;border-bottom:1px solid var(--line);padding-bottom:8px}

.pagination{display:flex;justify-content:center;gap:6px;margin-top:20px}
.pagination a{width:30px;height:30px;border:1px solid var(--line);display:flex;align-items:center;justify-content:center;font-size:12px;color:var(--grey)}
.pagination a.current{background:var(--blue);border-color:var(--blue);color:#fff}

/* sidebar */
.sidebar{width:260px}
.widget{margin-bottom:36px}
.widget-title{font-size:13px;font-weight:700;color:var(--blue);text-transform:uppercase;padding-bottom:10px;border-bottom:1px solid var(--line);margin-bottom:10px}
.cat-list{list-style:none}
.cat-list li{font-size:12.5px;padding:6px 0 6px 14px;position:relative;border-bottom:1px solid #f0f2f5}
.cat-list li::before{content:"";position:absolute;left:2px;top:13px;width:5px;height:5px;background:var(--red)}
.popular li{list-style:none;font-size:12.5px;color:var(--grey-dark);padding:6px 0;border-bottom:1px solid #f0f2f5;line-height:1.5}
.popular li span{color:#a5adb5;font-size:11px}

/* footer */
.site-footer{position:absolute;left:0;top:2200px;width:1200px;height:200px;background:var(--footer);color:var(--footer-text)}
.site-footer .container{display:flex;justify-content:space-between;padding-top:30px}
.footer-col{width:250px}
.footer-title{font-size:13px;font-weight:700;color:var(--red);margin-bottom:14px}
.footer-col p{font-size:12px;line-height:1.6}
.mini-post{display:flex;gap:10px;margin-bottom:12px;font-size:11.5px;line-height:1.5}
.mini-date{width:40px;height:40px;flex:none;background:#fff;color:var(--blue);text-align:center;font-weight:700;font-size:15px;line-height:1;padding-top:6px}
.mini-date small{display:block;font-size:9px;font-weight:400;color:var(--grey);margin-top:2px}
.thumb-grid{display:grid;grid-template-columns:repeat(4,52px);gap:6px}
.thumb-grid div{height:52px;background:linear-gradient(160deg,#7b8a99,#3d6a45)}
.thumb-grid div:nth-child(3n){background:linear-gradient(160deg,#9b4a4c,#4b7a3c)}
.social{display:flex;gap:8px;margin-top:16px}
.social span{width:30px;height:30px;background:#3f76ad;border:1px solid #5a8cc0}
.footer-bar{position:absolute;left:0;top:2400px;width:1200px;height:68px;background:#fff;border-top:1px solid var(--line)}
.footer-bar .container{height:68px;display:flex;align-items:center;justify-content:space-between;font-size:11px;color:#8a96a2}
.footer-bar b{color:var(--red);font-weight:400}
.footer-links{display:flex;gap:16px;color:var(--grey-dark)}
</style>
</head>
<body>

<header class="site-header">
  <div class="container">
    <a class="brand" href="#"><span class="brand-mark"></span><span class="brand-name">Northgate Harriers</span></a>
    <nav class="main-nav">
      <a href="#"><svg viewBox="0 0 20 20"><path d="M10 2 1 10h3v8h5v-5h2v5h5v-8h3z"/></svg>Home</a>
      <a href="#"><svg viewBox="0 0 20 20"><circle cx="10" cy="6" r="4"/><path d="M2 19c0-5 4-7 8-7s8 2 8 7z"/></svg>About us</a>
      <a href="#"><svg viewBox="0 0 20 20"><rect x="2" y="2" width="7" height="7"/><rect x="11" y="2" width="7" height="7"/><rect x="2" y="11" width="7" height="7"/><rect x="11" y="11" width="7" height="7"/></svg>Portfolio</a>
      <a href="#" class="active"><svg viewBox="0 0 20 20"><path d="M3 3h14v11H8l-5 4z"/></svg>Blog</a>
      <a href="#"><svg viewBox="0 0 20 20"><path d="M10 1l2.6 6 6.4.5-4.9 4.2 1.5 6.3L10 14.6 4.4 18l1.5-6.3L1 7.5 7.4 7z"/></svg>Features</a>
      <a href="#"><svg viewBox="0 0 20 20"><path d="M2 4h16v12H2zm1 1 7 6 7-6"/></svg>Contact</a>
      <a href="#" class="search"><svg viewBox="0 0 20 20"><circle cx="8" cy="8" r="5" fill="none" stroke="#5c5c5c" stroke-width="2"/><path d="M12 12l6 6" stroke="#5c5c5c" stroke-width="2.5"/></svg></a>
    </nav>
  </div>
</header>

<section class="page-band">
  <div class="container">
    <h1 class="page-title">Blog</h1>
    <span class="page-tagline">Checkout the latest news from our team</span>
    <span class="breadcrumb">You are here: <b>Blog</b> / Blog default</span>
  </div>
</section>

<div class="container content">
  <main class="posts">

    <article class="post">
      <div class="post-media">
        <div class="photo field" role="img" aria-label="Photo of sevens players in red jerseys running on a grass pitch"></div>
        <div class="date-badge"><span class="day">31</span><span class="month">May</span><span class="type"><svg viewBox="0 0 20 20"><path d="M2 5h4l2-2h4l2 2h4v12H2z"/></svg></span></div>
      </div>
      <div class="post-body">
        <h2 class="post-title">Beautiful vintage style</h2>
        <p class="post-meta">Posted by <b>Mark</b> · 1 comments</p>
        <p class="post-excerpt">Sed ut perspiciatis unde omnis iste natus error sit voluptatem accusantium doloremque laudantium, totam rem aperiam, eaque ipsa quae ab illo inventore veritatis et.</p>
        <a class="read-more" href="#">Continue reading »</a>
      </div>
    </article>

    <article class="post">
      <div class="post-media">
        <div class="photo stadium" role="img" aria-label="Photo of a packed stadium during a sevens match"></div>
        <div class="date-badge"><span class="day">22</span><span class="month">Apr</span><span class="type"><svg viewBox="0 0 20 20"><path d="M2 5h4l2-2h4l2 2h4v12H2z"/></svg></span></div>
      </div>
      <div class="post-body">
        <h2 class="post-title">Second blog post with image</h2>
        <p class="post-meta">Posted by <b>Mark</b> · 1 comments</p>
        <p class="post-excerpt">Sed ut perspiciatis unde omnis iste natus error sit voluptatem accusantium doloremque laudantium, totam rem aperiam, eaque ipsa quae ab illo inventore veritatis et.</p>
        <a class="read-more" href="#">Continue reading »</a>
      </div>
    </article>

    <article class="post">
      <div class="post-media">
        <div class="photo video" role="img" aria-label="Embedded video still on a red background"></div>
        <div class="player-bar"><span class="play"></span><span class="track"><i></i></span></div>
        <div class="date-badge"><span class="day">12</span><span class="month">Mar</span><span class="type"><svg viewBox="0 0 20 20"><path d="M6 4l10 6-10 6z"/></svg></span></div>
      </div>
      <div class="post-body">
        <h2 class="post-title">Post with ClipVault video</h2>
        <p class="post-meta">Posted by <b>Admin</b> · 1 comments</p>
        <p class="post-excerpt">Sed ut perspiciatis unde omnis iste natus error sit voluptatem accusantium doloremque laudantium, totam rem aperiam, eaque ipsa quae ab illo inventore veritatis et.</p>
        <p class="post-caption">Match clip from our spring training camp</p>
        <a class="read-more" href="#">Continue reading »</a>
      </div>
    </article>

    <article class="post">
      <div class="post-media">
        <div class="photo scrum" role="img" aria-label="Photo of a scrum in front of stadium advertising boards"></div>
        <div class="date-badge"><span class="day">31</span><span class="month">Jan</span><span class="type"><svg viewBox="0 0 20 20"><path d="M6 4l10 6-10 6z"/></svg></span></div>
      </div>
      <div class="post-body">
        <h2 class="post-title">Post with video in lightbox</h2>
        <p class="post-meta">Posted by <b>Admin</b> · 1 comments</p>
        <p class="post-excerpt">Sed ut perspiciatis unde omnis iste natus error sit voluptatem accusantium doloremque laudantium, totam rem aperiam, eaque ipsa quae ab illo inventore veritatis et.</p>
        <a class="read-more" href="#">Continue reading »</a>
      </div>
    </article>

    <article class="post">
      <div class="post-media">
        <div class="photo night" role="img" aria-label="Photo of a floodlit match seen from the stands"></div>
        <div class="date-badge"><span class="day">31</span><span class="month">Dec</span><span class="type"><svg viewBox="0 0 20 20"><path d="M8 3v10a3 3 0 1 0 2 3V7h6V3z"/></svg></span></div>
      </div>
      <div class="post-body">
        <h2 class="post-title">Cool jazz cover</h2>
        <p class="post-meta">Posted by <b>Mark</b> · 1 comments</p>
        <p class="post-excerpt">Sed ut perspiciatis unde omnis iste natus error sit voluptatem accusantium doloremque laudantium, totam rem aperiam, eaque ipsa quae ab illo inventore veritatis et.</p>
        <a class="read-more" href="#">Continue reading »</a>
      </div>
    </article>

    <nav class="pagination">
      <a href="#" class="current">1</a><a href="#">2</a><a href="#">3</a><a href="#">4</a><a href="#">5</a><a href="#">»</a>
    </nav>
  </main>

  <aside class="sidebar">
    <section class="widget">
      <h3 class="widget-title">Blog categories</h3>
      <ul class="cat-list">
        <li>Web Design</li><li>Motion Graphics</li><li>Photography</li><li>Uncategorized</li>
      </ul>
    </section>
    <section class="widget">
      <h3 class="widget-title">Popular posts</h3>
      <ul class="popular">
        <li>Lorem ipsum dolor sit amet, consectetur adipiscing elit, sed diam nonummy nibh euismod <span>| 22 APR, Web Design</span></li>
        <li>Consectetur adipiscing elit, sed diam nonummy nibh <span>| 12 MAR, Photography</span></li>
        <li>Beauty in Red <span>| 31 MAY, Motion Graphics</span></li>
      </ul>
    </section>
    <section class="widget">
      <h3 class="widget-title">Chirpline widget</h3>
    </section>
  </aside>
</div>

<footer class="site-footer">
  <div class="container">
    <div class="footer-col">
      <h4 class="footer-title">Sliding text article</h4>
      <p>Sed ut perspiciatis unde omnis iste natus error sit voluptatem accusantium doloremque laudantium, totam rem aperiam, eaque ipsa quae ab illo inventore veritatis et.</p>
    </div>
    <div class="footer-col">
      <h4 class="footer-title">Latest blog articles</h4>
      <div class="mini-post"><span class="mini-date">22<small>APR</small></span><span>Sed ut perspiciatis unde omnis iste | Web design</span></div>
      <div class="mini-post"><span class="mini-date">12<small>MAR</small></span><span>Sed ut perspiciatis unde omnis iste | Photography</span></div>
    </div>
    <div class="footer-col">
      <h4 class="footer-title">Team photo stream</h4>
      <div class="thumb-grid" role="img" aria-label="Grid of small team match photos">
        <div></div><div></div><div></div><div></div><div></div><div></div><div></div><div></div>
      </div>
    </div>
    <div class="footer-col">
      <h4 class="footer-title">Contact us</h4>
      <p>You can reach us on social networks, or send us a message through our contact form.</p>
      <div class="social"><span></span><span></span><span></span><span></span><span></span></div>
    </div>
  </div>
</footer>

<div class="footer-bar">
  <div class="container">
    <span>Copyright © Northgate Harriers 2013. All rights reserved. Theme by <b>Fieldhouse Studio</b></span>
    <nav class="footer-links"><a href="#">Home</a><a href="#">Pages</a><a href="#">Portfolio</a><a href="#">Blog</a><a href="#">Features</a><a href="#">Contact</a></nav>
  </div>
</div>

</body>
</html>
```